Vastmere Holdings Webpage Design

We need a new website for our company. The company is Vastmere Holdings Pty Ltd. We are in the business of Asbestos Removal; Demolition; Earthworks and Transport. We do not advertise and would like our website to be a reference point for our clients / potential clients and also to make our services known to those searching the internet for the services we offer. Some examples of the style of website we are after are:
http://www.quorrintdemolition.com.au/
http://m.feltrovindemolitions.com.au/
http://www.pinsettodemolition.com.au
http://www.rulqa.com.au
http://www.tjhservices.com.au
http://www.steadfield-deconstruction.com.au
We will need to work on content. Enclosed is an example. We also need to purchase the domain vastmereholdings.com.au and need to set up email accounts and ensure the website is mobile friendly. We have a company logo and have built our business on delivering professional, quality services on time. We would like the webpage to be simple, informative and professional - black and white / grey themed. We would also like to add a photo gallery etc later.

Industry/Entity Type

Construction

Coding

Coded - Design and coding required

Number of Pages Required

1 page

Colors
000000
fcfcfc
959595
dddddd

Requirements
Must have
• Information regarding the services we provide

```html
<!DOCTYPE html>
<html lang="en">
<head>
<meta charset="utf-8">
<title>Vastmere Holdings</title>
<link href="https://fonts.googleapis.com/css2?family=Rajdhani:wght@500;600&family=Raleway:wght@400;500&display=swap" rel="stylesheet">
<style>
:root{
  --black:#000;--ink:#222;--dark:#2f2f2f;--darker:#262626;--grey:#959595;--light:#dddddd;--paper:#fcfcfc;--text:#444;
}
*{margin:0;padding:0;box-sizing:border-box}
html,body{width:814px;height:1200px;overflow:hidden;background:var(--paper);font-family:"Raleway",sans-serif;color:var(--text)}
.page{position:relative;width:814px;height:1200px;overflow:hidden;background:#f1f1f1}
.abs{position:absolute}
.head-tab{left:0;top:0;width:330px;height:86px;background:#777;clip-path:polygon(0 0,100% 0,100% 58%,96% 100%,0 100%)}
.head-white{left:110px;top:0;width:704px;height:50px;background:linear-gradient(#fff,#ececec);border-radius:25px 0 0 25px}
.brand{left:132px;top:10px;font-family:"Rajdhani",sans-serif;font-weight:600;font-size:22px;letter-spacing:5px;color:var(--ink)}
.nav{left:310px;top:50px;width:504px;height:28px;background:linear-gradient(#333,#111);display:flex;align-items:center;padding-left:18px}
.nav a{font-family:"Rajdhani",sans-serif;font-size:11px;color:#fff;text-decoration:none;padding:0 12px;border-right:1px solid #444;line-height:14px}
.nav a:last-child{border:0}
.nav .on{position:relative}
.nav .on::after{content:"";position:absolute;left:6px;right:6px;top:20px;height:3px;border-radius:2px;background:var(--grey)}
.call{left:120px;top:57px;display:flex;align-items:center;gap:6px;color:#fff;font-family:"Rajdhani",sans-serif;font-size:11px}
.call b{font-weight:500;font-size:16px}
.call .ring{width:22px;height:22px;border:1px solid #ccc;border-radius:50%;display:flex;align-items:center;justify-content:center}
.social{display:flex;gap:11px}
.social span{width:20px;height:20px;border-radius:50%;border:2px solid #ddd;background:#555;display:block}
.hero{left:0;top:78px;width:814px;height:430px;background:linear-gradient(180deg,#7fa9d8 0%,#b9cde0 45%,#b5643a 62%,#a4492a 100%)}
.caption{left:110px;top:237px;width:375px;height:70px;background:rgba(20,20,20,.82);border-left:6px solid #ccc;clip-path:polygon(0 0,100% 0,94% 100%,0 100%);padding:4px 10px;font-family:"Rajdhani",sans-serif;font-style:italic;font-size:16px;line-height:21px;color:#fff}
.arrow{top:258px;font-family:"Rajdhani",sans-serif;font-size:38px;color:#eee;line-height:1}
.main{left:110px;top:440px;width:594px;height:560px;background:#fff;box-shadow:0 0 8px rgba(0,0,0,.15)}
.services{left:110px;top:440px;width:594px;height:152px;display:flex;background:linear-gradient(#fff,#e9e9e9)}
.svc{flex:1;position:relative;text-align:center;border-right:1px solid #ddd;padding:64px 6px 0}
.svc:last-child{border:0}
.svc h3{font-family:"Rajdhani",sans-serif;font-weight:500;font-size:15px;line-height:18px;color:var(--ink);margin-bottom:3px}
.svc p{font-size:7.6px;line-height:11.3px;color:#555}
.plus{position:absolute;left:50%;bottom:-7px;width:14px;height:14px;margin-left:-7px;background:#333;color:#fff;font-size:13px;line-height:13px;font-weight:500}
.badge{position:absolute;left:50%;top:-57px;width:114px;height:114px;margin-left:-57px;border-radius:50%;background:conic-gradient(from 90deg,var(--dark) 0 180deg,transparent 180deg)}
.badge i{position:absolute;left:16px;top:16px;width:82px;height:82px;border-radius:50%;background:#fff;display:flex;align-items:center;justify-content:center}
.about{left:110px;top:632px;width:594px;text-align:center}
.about h2{font-family:"Rajdhani",sans-serif;font-weight:500;font-size:22px;color:var(--ink)}
.about h2 span{font-weight:600}
.about hr{width:220px;margin:4px auto 18px;border:0;height:1px;background:linear-gradient(90deg,transparent,#ccc,transparent)}
.about p{font-size:8.2px;line-height:14.4px;color:#444;padding:0 10px;margin-bottom:14px}
.tile{top:792px;width:277px;height:178px;color:#fff;text-align:center;padding-top:80px}
.tile h4{font-family:"Rajdhani",sans-serif;font-weight:500;font-size:21px}
.tile p{font-size:8px;line-height:14px;padding:0 16px}
.safety{left:120px;background:linear-gradient(160deg,#1b3d7e,#4f77b2 60%,#9eb5d1)}
.env{left:417px;background:radial-gradient(circle at 50% 55%,#6b6a4a,#2e2c22 75%)}
.footer-wave{left:0;top:950px;width:814px;height:250px}
.fcol{top:1060px;color:#eee}
.fcol h5{font-family:"Rajdhani",sans-serif;font-weight:500;font-size:11px;padding-bottom:4px;border-bottom:1px solid #555;margin-bottom:10px}
.links{list-style:none;font-size:7.5px;line-height:13.7px}
.links li::before{content:"›";margin-right:8px}
.contact{display:grid;grid-template-columns:114px 100px;row-gap:8px;font-size:7.2px;line-height:9.5px}
.contact em{display:block;font-size:6.6px;color:#bbb}
.ci{display:flex;gap:6px}
.ci svg{flex:none;margin-top:1px}
.hours{font-size:7px;line-height:12px;text-align:center;width:116px;margin-left:-2px}
.copy{left:0;top:1173px;width:814px;height:27px;background:#1f1f1f;color:#ddd;font-size:7.5px;padding:8px 120px}
</style>
</head>
<body>
<div class="page">
  <div class="abs head-tab"></div>
  <div class="abs head-white"></div>
  <div class="abs brand">VASTMERE</div>
  <div class="abs social" style="left:586px;top:14px"><span></span><span></span><span></span><span></span></div>
  <div class="abs call"><span class="ring"><svg width="10" height="10" viewBox="0 0 10 10"><path d="M2 1l2 2-1 1.2c.6 1.2 1.5 2.1 2.8 2.8L7 6l2 2-1.4 1.4C4.5 9 1 5.5.6 2.4z" fill="#fff"/></svg></span>CALL US NOW : <b>0198 765 432</b></div>
  <nav class="abs nav"><a class="on">Home</a><a>About Us</a><a>Our Services</a><a>Safety</a><a>Environment</a><a>Contact Us</a></nav>

  <div class="abs hero" role="img" aria-label="Photo of a backhoe loader and workers in hi-vis digging a trench in red soil"></div>
  <div class="abs caption">Vastmere Transport and Demolition offer an extensive range of services including Demolition, Earthworks and Asbestos Removal.</div>
  <div class="abs arrow" style="left:52px">«</div>
  <div class="abs arrow" style="left:734px">»</div>

  <div class="abs main"></div>
  <div class="abs services">
    <div class="svc"><div class="badge"><i><svg width="44" height="40" viewBox="0 0 44 40"><path d="M8 4l22 14v12H22V22zM8 4v20" stroke="#222" stroke-width="3" fill="none"/><circle cx="8" cy="30" r="6" fill="#222"/><rect x="24" y="33" width="18" height="5" rx="2" fill="#222"/></svg></i></div><h3>Demolition</h3><p>Vastmere Transport and Demolition provide an extensive range of demolition services.</p><span class="plus">+</span></div>
    <div class="svc"><div class="badge"><i><svg width="48" height="34" viewBox="0 0 48 34"><rect x="4" y="8" width="20" height="12" fill="#222"/><path d="M24 12l12-8 8 12" stroke="#222" stroke-width="3" fill="none"/><rect x="2" y="22" width="26" height="6" rx="3" fill="#222"/><path d="M0 32h48" stroke="#222" stroke-width="2"/></svg></i></div><h3>Earthworks</h3><p>Vastmere Transport and Demolition possess all necessary equipment and skilled personnel to provide earthmoving services.</p><span class="plus">+</span></div>
    <div class="svc"><div class="badge"><i><svg width="50" height="30" viewBox="0 0 50 30"><path d="M2 24L14 4l10 12 6-5 18 10-10 6H2z" stroke="#222" stroke-width="2.5" fill="none"/><path d="M10 16l5-8 5 8z" fill="#222"/></svg></i></div><h3>Asbestos Removal</h3><p>Naturally occurring silicate mineral made up of tiny fibres. When disturbed, it may produce a dust containing asbestos fibres.</p><span class="plus">+</span></div>
    <div class="svc"><div class="badge"><i><svg width="50" height="34" viewBox="0 0 50 34"><rect x="18" y="4" width="30" height="16" fill="#222"/><path d="M4 20V12l6-6h8v14z" fill="#222"/><rect x="2" y="20" width="46" height="4" fill="#222"/><circle cx="12" cy="28" r="5" fill="#222"/><circle cx="38" cy="28" r="5" fill="#222"/></svg></i></div><h3>Transport</h3><p>Hours of operation are generally assessed and implemented to meet the needs of each individual project.</p><span class="plus">+</span></div>
  </div>

  <section class="abs about">
    <h2>About <span>Vastmere Holdings</span></h2>
    <hr>
    <p>Vastmere Transport Pty Ltd was established by Director Daniel Harrow in 2002 with a focus providing services within the transport industry. Over time the company has developed and expanded to include the provision of Earthworks and Demolition. Daniel has over 10 years' experience working at all levels within these industries focusing primarily on Demolition and Earthworks in recent times.</p>
    <p>Vastmere Transport and Demolition is built on core values of Service, Safety and Environment and are dedicated to delivering a quality, safe, cost effective, efficient and reliable service.</p>
  </section>

  <div class="abs tile safety" role="img" aria-label="Photo of a safety first road sign against a blue sky"><h4>Safety</h4><p>The safety of our clients, workforce and wider community is of paramount importance to Vastmere Transport and Demolition.</p></div>
  <div class="abs tile env" role="img" aria-label="Photo of hands holding a green globe"><h4>Environment</h4><p>Vastmere Transport &amp; Demolition is committed to reducing the environmental impact of its undertakings.</p></div>

  <svg class="abs footer-wave" viewBox="0 0 814 250" preserveAspectRatio="none">
    <path d="M0 8C180 110 520 110 814 60V250H0z" fill="#2e2e2e"/>
    <path d="M160 88C420 140 640 100 814 30V52C650 110 420 132 160 88z" fill="#8c8c8c"/>
  </svg>

  <div class="abs fcol" style="left:120px;width:100px"><h5>Quick Links</h5>
    <ul class="links"><li>Home</li><li>About Us</li><li>Services</li><li>Safety</li><li>Environment</li><li>Contact Us</li></ul></div>
  <div class="abs fcol" style="left:229px;width:200px"><h5>Contact Information</h5>
    <div class="contact">
      <div class="ci"><svg width="8" height="8" viewBox="0 0 8 8"><circle cx="4" cy="2.3" r="2" fill="#ddd"/><path d="M0 8c0-3 8-3 8 0z" fill="#ddd"/></svg><div>Daniel Harrow<em>Director</em></div></div>
      <div class="ci"><svg width="8" height="8" viewBox="0 0 8 8"><circle cx="4" cy="2.3" r="2" fill="#ddd"/><path d="M0 8c0-3 8-3 8 0z" fill="#ddd"/></svg><div>Mira Telford<em>Administration</em></div></div>
      <div class="ci"><svg width="8" height="9" viewBox="0 0 8 9"><path d="M4 9C1 5 1 4 1 3a3 3 0 016 0c0 1 0 2-3 6z" fill="#ddd"/></svg><div>Po Box 512 Calderwick Qld 4391 Calderwick Qld 4391</div></div>
      <div class="ci"><svg width="8" height="9" viewBox="0 0 8 9"><path d="M4 9C1 5 1 4 1 3a3 3 0 016 0c0 1 0 2-3 6z" fill="#ddd"/></svg><div>PO Box 512</div></div>
      <div class="ci"><svg width="8" height="8" viewBox="0 0 10 10"><path d="M2 1l2 2-1 1.2c.6 1.2 1.5 2.1 2.8 2.8L7 6l2 2-1.4 1.4C4.5 9 1 5.5.6 2.4z" fill="#ddd"/></svg><div>0198 765 432</div></div>
      <div class="ci"><svg width="8" height="8" viewBox="0 0 10 10"><path d="M2 1l2 2-1 1.2c.6 1.2 1.5 2.1 2.8 2.8L7 6l2 2-1.4 1.4C4.5 9 1 5.5.6 2.4z" fill="#ddd"/></svg><div>0198 765 432</div></div>
      <div class="ci"><svg width="9" height="7" viewBox="0 0 9 7"><rect width="9" height="7" fill="#ddd"/><path d="M0 0l4.5 4L9 0" stroke="#2e2e2e" fill="none"/></svg><div>info@vastmere.com.au</div></div>
      <div class="ci"><svg width="9" height="7" viewBox="0 0 9 7"><rect width="9" height="7" fill="#ddd"/><path d="M0 0l4.5 4L9 0" stroke="#2e2e2e" fill="none"/></svg><div>info@vastmere.com.au</div></div>
    </div></div>
  <div class="abs fcol" style="left:448px;width:112px;top:1062px"><h5>Hours of Operation</h5>
    <p class="hours">Vastmere Transport and Demolition operate Monday to Saturday.Hours of operation are generally assessed and implemented to meet the needs of each individual project.</p></div>
  <div class="abs fcol" style="left:580px;width:114px;top:1062px"><h5>Follow Us</h5>
    <div class="social" style="margin:6px 0 0 6px;gap:9px"><span></span><span></span><span></span><span></span></div>
    <div style="margin:16px 0 0 9px;font-family:'Rajdhani',sans-serif;font-weight:600;font-size:12px;letter-spacing:3px">VASTMERE</div></div>

  <div class="abs copy">Copyright © 2015 Vastmere Holdings All Right Reserved</div>
</div>
</body>
</html>
```